International IT and cyber security consulting company is looking to establish a web presence.

Harwell Mariner Advisory LLC provides IT, cyber security, risk, project management and data analytics consulting services worldwide. Our clients are both government and corporate. We are looking to establish a basic web presence with about 6 pages (Home, About Harwell, Our Experts, News and Events, Careers, Contact Us). The designs should set the look and feel of the site for further build out down the line. The final design should be straightforward and simple and allow us to convey information about our consulting services clearly.

Target Market(s)

Government and corporate clients or potential clients, job seekers.

Industry/Entity Type

Consulting

Contact Information for Business Card

The cards will have english on the front and arabic on the back. The design should be the same on both sides.

Coding

Number of Pages Required

Font styles to use
Serif
Sans Serif

Requirements
Must have
• The pages should be simple but visually appealing with a picture or graphic that is appropriate to the company or services we offer. Our name and logo should be branded throughout the design. While we are mostly an IT company we also have a line of business where we organize speaking events for VIPs so the website shouldn't overly emphasize our IT work.
Should not have
• No cartoons or drawings. The site should not have overly flashy or loud colors. We cater to a conservative set of clients so the site should match what they expect to see in an international consultancy's website. There should not be an overuse of the color orange because it can be hard on the eyes if it is used too much on the page. Also, please do not use graphics or pictures that use locks, keys, castles, shields etc since these are too commonly used in the cyber security industry.

```html
<!DOCTYPE html>
<html lang="en">
<head>
<meta charset="utf-8">
<title>Harwell Mariner Advisory LLC</title>
<link href="https://fonts.googleapis.com/css2?family=Cinzel:wght@400;600&family=Poppins:wght@300;400;500;600&display=swap" rel="stylesheet">
<style>
:root{
  --orange:#f7871f;
  --orange-deep:#e8721a;
  --ink:#2b2b2b;
  --muted:#555;
  --light:#eeeeee;
  --paper:#ffffff;
  --footer:#1f1f21;
  --navy:#0a2a4a;
}
*{box-sizing:border-box;margin:0;padding:0}
html,body{width:1200px;height:4243px;overflow:hidden}
body{font-family:"Poppins",sans-serif;color:var(--ink);background:var(--paper);position:relative}
.serif{font-family:"Cinzel",serif}
section,header,footer{position:absolute;left:0;width:1200px}
.abs{position:absolute}

/* header */
.site-header{top:0;height:98px;background:var(--paper)}
.brand{left:80px;top:14px;font-family:"Cinzel",serif;color:var(--orange);line-height:1}
.brand .name{font-size:28px;font-weight:600}
.brand .sub{font-size:17px;color:#888;letter-spacing:1px;margin-top:4px}
.phone{right:66px;top:16px;font-size:16px;display:flex;align-items:center;gap:8px}
.phone .dot{width:30px;height:30px;border-radius:50%;background:var(--orange);display:flex;align-items:center;justify-content:center}
.nav{left:475px;top:58px;display:flex;gap:34px;font-size:16px}
.nav a{color:var(--ink);text-decoration:none;padding-bottom:10px}
.nav a.active{color:var(--orange);border-bottom:2px solid var(--orange)}

/* hero */
.hero{top:98px;height:700px;background:radial-gradient(ellipse at 70% 35%,#1f8fd6 0%,#0d4f8a 35%,#062543 70%,#03162b 100%)}
.hero .kicker{left:132px;top:175px;color:#fff;font-size:22px;font-family:"Cinzel",serif}
.hero h1{left:130px;top:212px;color:#fff;font-family:"Cinzel",serif;font-weight:600;font-size:40px;line-height:46px}
.hero p{left:132px;top:330px;width:460px;color:#fff;font-size:15px;line-height:24px}
.btn{display:inline-flex;align-items:center;gap:12px;border-radius:30px;font-size:18px;color:#fff;background:var(--orange)}
.btn .ring{width:22px;height:22px;border-radius:50%;border:2px solid currentColor;display:inline-flex;align-items:center;justify-content:center;font-size:12px}
.hero .btn{left:132px;top:430px;height:48px;padding:0 26px}
.hero .arrow{top:298px;width:48px;height:48px;border-radius:50%;display:flex;align-items:center;justify-content:center}
.hero .prev{left:1007px;border:2px solid rgba(255,255,255,.6)}
.hero .next{left:1068px;background:var(--orange)}

/* services */
.services{top:798px;height:526px;background:var(--paper)}
.service{top:90px;width:235px;text-align:center}
.service .icon{width:124px;height:124px;margin:28px auto 0;border:2px dashed var(--orange);border-radius:50%;position:relative}
.service .icon::after{content:"";position:absolute;inset:30px;border:3px solid var(--orange);border-radius:8px}
.service h3{font-size:20px;font-weight:500;margin-top:18px}
.service p{font-size:13px;color:var(--muted);line-height:19px;margin:8px auto 0;width:200px}
.service.featured{border:2px solid #ccc;border-radius:4px;height:344px}
.service.featured .btn{font-size:12px;height:28px;padding:0 14px;margin-top:18px;gap:8px}
.service.featured .btn .ring{width:16px;height:16px;font-size:9px}

/* welcome */
.welcome{top:1324px;height:700px;background:var(--light)}
.welcome .visual{left:83px;top:11px;width:510px;height:510px;border-radius:50%;background:radial-gradient(circle at 48% 48%,#c9541a 0%,#7a3a1c 12%,#fafafa 32%,#f2f2f2 100%)}
.welcome .kicker{left:644px;top:140px;font-family:"Cinzel",serif;font-size:26px}
.welcome h2{left:644px;top:178px;font-family:"Cinzel",serif;font-weight:600;font-size:42px}
.welcome p{left:644px;top:244px;width:438px;font-size:14.5px;line-height:21.5px;color:#333}
.welcome .btn{left:642px;top:386px;height:53px;padding:0 30px;background:transparent;color:var(--orange);border:2px solid var(--orange)}

/* orange band */
.band{top:1870px;height:1014px}
.band svg.bg{position:absolute;left:0;top:0}
.experts-title{left:165px;top:255px;color:#fff;font-family:"Cinzel",serif;font-weight:600;font-size:44px}
.experts-text{left:165px;top:315px;width:350px;color:#fff;font-size:13.5px;line-height:27px}
.experts-nav{left:165px;top:414px;display:flex;gap:14px}
.experts-nav span{width:32px;height:32px;border-radius:50%;display:flex;align-items:center;justify-content:center;color:#fff;font-size:14px}
.experts-nav .o{border:2px solid #fff}
.experts-nav .f{background:#8a4a14}
.expert{top:178px;width:176px;height:345px;background:#fff;border-radius:88px;text-align:center;box-shadow:0 6px 14px rgba(0,0,0,.15)}
.expert .photo{width:150px;height:150px;border-radius:50%;margin:14px auto 0;background:linear-gradient(160deg,#d9dde2,#7e8893)}
.expert h4{font-size:15px;font-weight:500;margin-top:20px}
.expert .role{font-size:12px;color:var(--muted);margin-top:6px;line-height:15px;height:30px}
.expert .social{width:28px;height:28px;border-radius:50%;background:#1d63b4;margin:14px auto 0}
.why-title{left:0;width:1200px;top:590px;text-align:center;color:#fff;font-family:"Cinzel",serif;font-weight:600;font-size:42px}
.why{top:693px;width:300px;text-align:center;color:#fff}
.why .ring{width:96px;height:96px;border:3px solid #fff;border-radius:50%;margin:0 auto;display:flex;align-items:center;justify-content:center}
.why h3{font-size:21px;font-weight:400;margin-top:18px}
.why p{font-size:13px;line-height:19px;margin:12px auto 0;width:200px}

/* news */
.news{top:2884px;height:610px;background:#fff}
.news h2{left:0;width:1200px;top:62px;text-align:center;font-family:"Cinzel",serif;font-weight:600;font-size:42px}
.card{top:138px;width:293px;height:380px;background:#fff;box-shadow:0 2px 12px rgba(0,0,0,.12)}
.card .img{position:absolute;left:0;width:293px;height:173px}
.card .date{position:absolute;width:100px;height:38px;background:var(--orange);color:#fff;display:flex;align-items:center;gap:8px;padding-left:12px;clip-path:polygon(0 0,100% 0,86% 100%,0 100%)}
.card .date small{font-size:11px;line-height:11px;font-weight:600}
.card .date b{font-size:24px;font-weight:600}
.card .body{position:absolute;left:20px;width:260px}
.card h5{font-family:"Cinzel",serif;color:var(--orange);font-size:15.5px;font-weight:400;line-height:22px}
.card p{font-size:12.5px;line-height:19px;margin-top:10px;color:#333}
.card .more{display:inline-block;margin-top:12px;border:2px solid var(--orange);border-radius:20px;font-size:11px;font-weight:600;padding:6px 20px}

/* press */
.press{top:3494px;height:349px;background:#f3f3f3}
.press .cell{width:225px;height:107px;display:flex;align-items:center;justify-content:center}
.press .lbl{background:#fff;padding:12px 16px;font-size:23px;font-weight:600;color:#1a3d6d}
.press .cell.raised{background:#fff;box-shadow:0 4px 10px rgba(0,0,0,.15)}
.press .rule{height:1px;background:#ddd}
.press .vrule{width:1px;background:#ddd}

/* footer */
.site-footer{top:3843px;height:400px;background:var(--footer);color:#fff}
.site-footer h6{font-size:19px;font-weight:600}
.f-item{display:flex;gap:12px;font-size:13.5px;line-height:18px}
.f-links a{display:block;color:#fff;text-decoration:none;font-size:13.5px;line-height:30px}
.socials{display:flex;gap:6px}
.socials span{width:32px;height:32px;border-radius:50%;border:1.5px solid #fff}
.field{position:absolute;border:1px solid #555;background:#2a2a2c;border-radius:3px;font-size:13px;color:#999;padding:10px 14px}
.send{position:absolute;left:626px;top:267px;width:104px;height:34px;background:var(--orange);border-radius:3px;font-size:14px;display:flex;align-items:center;justify-content:center}
.bottom-rule{left:0;top:325px;width:1200px;height:1px;background:#333}
.foot-brand{left:132px;top:338px;font-family:"Cinzel",serif;color:var(--orange);font-size:17px;line-height:16px}
.foot-brand small{display:block;font-size:11px;color:#aaa}
.copyright{right:117px;top:360px;font-size:13px}
</style>
</head>
<body>

<header class="site-header">
  <div class="brand abs">
    <div class="name">HARWELL MARINER</div>
    <div class="sub">ADVISORY LLC</div>
  </div>
  <div class="phone abs">
    <span class="dot"><svg width="14" height="14" viewBox="0 0 24 24"><path fill="#fff" d="M6.6 10.8a15 15 0 006.6 6.6l2.2-2.2c.3-.3.7-.4 1-.2 1.1.4 2.3.6 3.6.6.6 0 1 .4 1 1V20c0 .6-.4 1-1 1A17 17 0 013 4c0-.6.4-1 1-1h3.5c.6 0 1 .4 1 1 0 1.3.2 2.5.6 3.6.1.3 0 .7-.2 1z"/></svg></span>
    555 010 2040
  </div>
  <nav class="nav abs">
    <a class="active" href="#">Home</a><a href="#">About Us</a><a href="#">Our Experts</a><a href="#">News &amp; Events</a><a href="#">Careers</a><a href="#">Contact Us</a>
  </nav>
</header>

<section class="hero" role="img" aria-label="Glowing blue digital chain links on a dark technology background">
  <div class="kicker abs">A Technology Consultant</div>
  <h1 class="abs">That Solves Real World<br>Business Problems</h1>
  <p class="abs">Lorem Ipsum is simply dummy text of the printing and typesetting industry. Lorem Ipsum has been the industry's standard dummy text ever since</p>
  <a class="btn abs">Get In Touch <span class="ring">›</span></a>
  <div class="arrow prev abs"><svg width="18" height="18" viewBox="0 0 24 24"><path d="M15 5l-7 7 7 7" stroke="#fff" stroke-width="2" fill="none"/></svg></div>
  <div class="arrow next abs"><svg width="18" height="18" viewBox="0 0 24 24"><path d="M9 5l7 7-7 7" stroke="#fff" stroke-width="2.5" fill="none"/></svg></div>
</section>

<section class="services">
  <div class="service abs" style="left:110px"><div class="icon"></div><h3>Cyber Security</h3><p>Lorem Ipsum is simply dummy text of the printing and typesetting industry.</p></div>
  <div class="service featured abs" style="left:348px;top:88px"><div class="icon"></div><h3>Data Analytics</h3><p>Lorem Ipsum is simply dummy text of the printing and typesetting industry.</p><a class="btn">Get In Touch <span class="ring">›</span></a></div>
  <div class="service abs" style="left:597px"><div class="icon"></div><h3>Project Management</h3><p>Lorem Ipsum is simply dummy text of the printing and typesetting industry.</p></div>
  <div class="service abs" style="left:850px"><div class="icon"></div><h3>Risk Management</h3><p>Lorem Ipsum is simply dummy text of the printing and typesetting industry.</p></div>
</section>

<section class="welcome">
  <div class="visual abs" role="img" aria-label="Network of connected glossy spheres around a glowing orange core"></div>
  <div class="kicker abs">Welcome To</div>
  <h2 class="abs">Harwell Security</h2>
  <p class="abs">Lorem Ipsum has been the industry's standard dummy text ever since the 1500s, when an unknown printer took a galley of type and scrambled it to make a type specimen book. It has survived not only five centuries, but also the leap into electronic typesetting, remaining essentially unchanged.</p>
  <a class="btn abs">Learn More <span class="ring">›</span></a>
</section>

<section class="band">
  <svg class="bg" width="1200" height="1014" viewBox="0 0 1200 1014"><polygon points="0,91 346,0 1200,149 1200,1014 0,1014" fill="#f7871f"/></svg>
  <div class="experts-title abs">Our Experts</div>
  <div class="experts-text abs">Lorem Ipsum is simply dummy text of the printing and typesetting industry. Lorem Ipsum has been the industry's standard dummy text</div>
  <div class="experts-nav abs"><span class="o">‹</span><span class="f">›</span></div>
  <div class="expert abs" style="left:572px"><div class="photo" role="img" aria-label="Portrait photo of an expert"></div><h4>ExpertsName</h4><div class="role">Managing Principal</div><div class="social"></div></div>
  <div class="expert abs" style="left:791px"><div class="photo" role="img" aria-label="Portrait photo of an expert"></div><h4>ExpertsName</h4><div class="role">Management<br>Consultant</div><div class="social"></div></div>

  <div class="why-title abs">Why Choose Us</div>
  <div class="why abs" style="left:162px"><div class="ring"><svg width="46" height="46" viewBox="0 0 24 24"><circle cx="14" cy="9" r="5" fill="none" stroke="#fff" stroke-width="2"/><path d="M10 13l-6 7" stroke="#fff" stroke-width="2.5"/></svg></div><h3>Professionalism</h3><p>Use our body field scanner, at home to uncover why yhou feelthe way you do</p></div>
  <div class="why abs" style="left:456px"><div class="ring"><svg width="46" height="46" viewBox="0 0 24 24"><circle cx="12" cy="12" r="9" fill="none" stroke="#fff" stroke-width="2"/><path d="M7 12l4 4 7-8" stroke="#fff" stroke-width="2.5" fill="none"/></svg></div><h3>Better Results</h3><p>Use our body field scanner, at home to uncover why yhou feelthe way you do</p></div>
  <div class="why abs" style="left:737px"><div class="ring"><svg width="46" height="46" viewBox="0 0 24 24"><g fill="none" stroke="#fff" stroke-width="2"><circle cx="6" cy="6" r="2"/><circle cx="18" cy="12" r="2"/><circle cx="6" cy="18" r="2"/><path d="M8 6h6a4 4 0 010 6M16 12H10a4 4 0 000 6"/></g></svg></div><h3>Quality Work</h3><p>Use our body field scanner, at home to uncover why yhou feelthe way you do</p></div>
</section>

<section class="news">
  <h2 class="abs">Latest News</h2>
  <div class="card abs" style="left:140px">
    <div class="img" style="top:0;background:linear-gradient(135deg,#0c2f4f,#1a6a9a 60%,#0a1f33)" role="img" aria-label="Hand touching a glowing digital data interface"></div>
    <div class="date" style="left:-8px;top:14px"><small>JAN<br>2020</small><b>18</b></div>
    <div class="body" style="top:195px"><h5>INDUSTRY'S STANDARD DUMMY TEXT EVER</h5><p>Lorem Ipsum is simply dummy text of the printing &amp; typesetting industry. Lorem Ipsum</p><span class="more">LEARN MORE</span></div>
  </div>
  <div class="card abs" style="left:457px">
    <div class="body" style="top:18px"><h5>INDUSTRY'S STANDARD DUMMY TEXT EVER</h5><p>Lorem Ipsum is simply dummy text of the printing &amp; typesetting industry. Lorem Ipsum</p><span class="more">LEARN MORE</span></div>
    <div class="img" style="top:207px;background:linear-gradient(135deg,#1b3552,#3b6a90 55%,#10233a)" role="img" aria-label="Digital globe with connected network points"></div>
    <div class="date" style="left:-8px;top:328px"><small>JAN<br>2020</small><b>18</b></div>
  </div>
  <div class="card abs" style="left:774px">
    <div class="img" style="top:0;background:linear-gradient(135deg,#e9ecef,#8c96a0 55%,#2f3942)" role="img" aria-label="Person using a laptop with a digital overlay"></div>
    <div class="date" style="left:-8px;top:14px"><small>JAN<br>2020</small><b>18</b></div>
    <div class="body" style="top:195px"><h5>INDUSTRY'S STANDARD DUMMY TEXT EVER</h5><p>Lorem Ipsum is simply dummy text of the printing &amp; typesetting industry. Lorem Ipsum</p><span class="more">LEARN MORE</span></div>
  </div>
</section>

<section class="press">
  <div class="rule abs" style="left:160px;top:183px;width:880px"></div>
  <div class="vrule abs" style="left:598px;top:75px;height:225px"></div>
  <div class="vrule abs" style="left:826px;top:75px;height:225px"></div>
  <div class="vrule abs" style="left:598px;top:75px;height:0"></div>
  <div class="cell abs" style="left:152px;top:70px"><span class="lbl">Ledgerline</span></div>
  <div class="cell raised abs" style="left:375px;top:70px"><span class="lbl" style="color:#111">Daily Quarry</span></div>
  <div class="cell abs" style="left:600px;top:70px"><span class="lbl" style="color:#111">Venture Weekly</span></div>
  <div class="cell abs" style="left:828px;top:70px"><span class="lbl" style="color:#111;font-size:20px">Meridian Business</span></div>
  <div class="cell abs" style="left:152px;top:192px"><span class="lbl" style="color:#111;font-size:21px">Nation Daily</span></div>
  <div class="cell abs" style="left:375px;top:192px"><span class="lbl" style="color:#111">Signal News</span></div>
  <div class="cell abs" style="left:600px;top:192px"><span class="lbl" style="color:#111">Daily Quarry</span></div>
  <div class="cell abs" style="left:828px;top:192px"><span class="lbl">Ledgerline</span></div>
</section>

<footer class="site-footer">
  <h6 class="abs" style="left:140px;top:52px">CONTACT US</h6>
  <div class="f-item abs" style="left:136px;top:96px"><svg width="14" height="18" viewBox="0 0 24 24"><path fill="#fff" d="M12 2a7 7 0 00-7 7c0 5 7 13 7 13s7-8 7-13a7 7 0 00-7-7zm0 9.5A2.5 2.5 0 1112 6a2.5 2.5 0 010 5.5z"/></svg><span>48 Harbor Lane Suite 4B<br>Sample 20012 TX</span></div>
  <div class="f-item abs" style="left:136px;top:158px;color:var(--orange)"><svg width="16" height="16" viewBox="0 0 24 24"><path fill="#fff" d="M6.6 10.8a15 15 0 006.6 6.6l2.2-2.2c.3-.3.7-.4 1-.2 1.1.4 2.3.6 3.6.6.6 0 1 .4 1 1V20c0 .6-.4 1-1 1A17 17 0 013 4c0-.6.4-1 1-1h3.5c.6 0 1 .4 1 1 0 1.3.2 2.5.6 3.6.1.3 0 .7-.2 1z"/></svg><span>(00) 000 0000 000</span></div>
  <div class="f-item abs" style="left:136px;top:203px"><svg width="16" height="16" viewBox="0 0 24 24"><path fill="#fff" d="M2 5h20v14H2zm2 2v.5l8 5 8-5V7z"/></svg><span>hello@harwellmariner.example</span></div>
  <div class="socials abs" style="left:134px;top:258px"><span></span><span></span><span></span><span></span></div>

  <h6 class="abs" style="left:430px;top:52px">COMPANY</h6>
  <div class="f-links abs" style="left:430px;top:83px"><a href="#">Home</a><a href="#">About Us</a><a href="#">Our Experts</a><a href="#">News &amp; Events</a><a href="#">Careers</a><a href="#">Contact Us</a></div>

  <div class="field" style="left:626px;top:63px;width:222px;height:36px">Name</div>
  <div class="field" style="left:853px;top:63px;width:214px;height:36px">Email</div>
  <div class="field" style="left:626px;top:108px;width:441px;height:36px">Subject</div>
  <div class="field" style="left:626px;top:153px;width:441px;height:98px">Message</div>
  <div class="send">Send</div>

  <div class="bottom-rule abs"></div>
  <div class="foot-brand abs">HARWELL MARINER<small>ADVISORY LLC</small></div>
  <div class="copyright abs">© 2020 Harwell Security. All Rights are Reserved.</div>
</footer>

</body>
</html>
```